Classy, Elegant, Simple Business Card Design

Looking to have a classy, simple, and elegant design. Want a top notch designed business card. I really like the look of the new brivo credit card. I also like the design I attached. I am trying to reach 21-29 year old females for booking us for there wedding or event. We offer Disc Jockey Service, Photo Booth Rentals, and Uplighting .

Target Market(s)

21-28 year old females

Contact Information for Business Card

Has to have logo, website, email, and phone number

Font styles to use
Other font styles liked:
• open to font choice, modern, clean
Designer to choose
33a6d7
0791cd
0555a3
ffffff

Requirements
Must have
• Has to have logo, website, email, and phone number
Nice to have
• I really like the design of the new brivo credit card. I also included my logo and some designs I like
Should not have
• clutter or too much info

```html
<!DOCTYPE html>
<html lang="en">
<head>
<meta charset="utf-8">
<title>Brightnote Event Group — Business Card</title>
<link href="https://fonts.googleapis.com/css2?family=Lato:wght@400;700&display=swap" rel="stylesheet">
<style>
  :root {
    --backdrop: #e9e6e2;
    --card-light: #ffffff;
    --card-edge: #c4c4c4;
    --ink: #2a2a2a;
    --ink-soft: #8c8c8c;
    --brand-blue: #0791cd;
    --brand-deep: #0555a3;
    --rule: #4a4a4a;
  }
  * { box-sizing: border-box; margin: 0; padding: 0; }
  html, body {
    width: 1200px; height: 900px; overflow: hidden;
    background: var(--backdrop);
    font-family: "Lato", Arial, sans-serif;
  }
  .card {
    position: absolute;
    width: 556px; height: 343px;
    background: radial-gradient(ellipse at 45% 50%, var(--card-light) 0%, #ececec 55%, var(--card-edge) 100%);
    box-shadow: 3px 4px 8px rgba(0,0,0,0.45);
    text-align: center;
    color: var(--ink);
  }
  .card--front { left: 330px; top: 90px; }
  .card--back { left: 330px; top: 470px; }

  .brand-name {
    font-weight: 700;
    color: var(--brand-deep);
    letter-spacing: 1px;
  }
  .card--front .brand-name { margin-top: 82px; font-size: 26px; }

  .contact-icons {
    margin: 24px auto 0;
    display: flex; align-items: center; justify-content: center; gap: 4px;
  }
  .contact-icons .rule { width: 52px; height: 1px; background: var(--rule); }
  .contact-icons svg { width: 22px; height: 22px; display: block; }

  .contact-list { list-style: none; margin-top: 10px; font-size: 16px; line-height: 20.5px; }
  .contact-list .web-accent { color: var(--brand-blue); }

  .divider { width: 182px; height: 1px; background: var(--rule); margin: 18px auto 0; }

  .services { margin-top: 18px; font-size: 16px; }

  .card--back .brand-block {
    position: absolute; left: 0; right: 0; top: 90px;
    display: flex; flex-direction: column; align-items: center; gap: 22px;
  }
  .brand-dot {
    width: 110px; height: 110px; border-radius: 50%;
    background: var(--brand-blue);
  }
  .card--back .brand-name { font-size: 28px; }
</style>
</head>
<body>
  <section class="card card--front">
    <p class="brand-name">BRIGHTNOTE EVENT GROUP</p>

    <div class="contact-icons">
      <span class="rule"></span>
      <svg viewBox="0 0 22 22" aria-label="Phone">
        <circle cx="11" cy="11" r="11" fill="#0791cd"/>
        <path d="M6 9 Q11 5 16 9 L14.5 10.5 L12.5 9.5 L9.5 9.5 L7.5 10.5 Z M7.5 12 H14.5 L15 16 H7 Z" fill="#fff"/>
      </svg>
      <svg viewBox="0 0 22 22" aria-label="Email">
        <circle cx="11" cy="11" r="11" fill="#0791cd"/>
        <rect x="5.5" y="7" width="11" height="8" fill="#fff"/>
        <path d="M5.5 7 L11 11.5 L16.5 7" fill="none" stroke="#0791cd" stroke-width="1"/>
      </svg>
      <svg viewBox="0 0 22 22" aria-label="Website">
        <circle cx="11" cy="11" r="11" fill="#0791cd"/>
        <circle cx="11" cy="11" r="5.5" fill="none" stroke="#fff" stroke-width="1.5"/>
        <path d="M11 5.5 V16.5 M5.5 11 H16.5" stroke="#fff" stroke-width="1.2"/>
      </svg>
      <span class="rule"></span>
    </div>

    <ul class="contact-list">
      <li>044-555 010 203</li>
      <li>info@brightnote.com</li>
      <li>www.<span class="web-accent">brightnoteevents</span>.com</li>
    </ul>

    <div class="divider"></div>

    <p class="services">Disc Jockey Service | Photo Booth Rentals | Uplighting</p>
  </section>

  <section class="card card--back">
    <div class="brand-block">
      <span class="brand-dot"></span>
      <p class="brand-name">BRIGHTNOTE EVENT GROUP</p>
    </div>
  </section>
</body>
</html>
```